Display Ad for Local Publication

We have never advertised before but now I would like to have an ad running in our local, community magazine. Our business is Cedar Hollow Mini Storage located in Port Ludlow, WA. PL is a small community (+/-2,500 people located across the Puget Sound from Seattle. The monthly magazine, The Tidings, covers all kinds of local news and activities and carries a number of ads from local businesses. Our is the only mini storage in Port Ludlow. We have enclosed storage units of various sizes and outdoor parking spaces for boats, trailers and RVs. I am enclosing a business card and the size requirements for Tidings advertisements. I want to develop a 1/8 page ad.

```html
<!DOCTYPE html>
<html lang="en">
<head>
<meta charset="utf-8">
<title>Cedar Hollow Mini Storage – Display Ad</title>
<link rel="stylesheet" href="https://fonts.googleapis.com/css2?family=Alfa+Slab+One&family=Poppins:wght@400;600;700&display=swap">
<style>
  :root {
    --navy: #231d5c;
    --green: #6cbf1f;
    --white: #ffffff;
    --page: #dfe0e2;
    --steel-light: #eef0f3;
    --steel-mid: #c9ccd2;
  }
  * { margin: 0; padding: 0; box-sizing: border-box; }
  html, body { width: 1200px; height: 820px; overflow: hidden; background: var(--page); }
  .ad {
    position: absolute; left: 132px; top: 121px;
    width: 936px; height: 579px;
    background: var(--white);
    overflow: hidden;
  }
  .headline-band {
    position: absolute; left: 0; top: 0; width: 100%; height: 121px;
    background: var(--navy);
    display: flex; align-items: center; justify-content: center;
  }
  .headline {
    font-family: "Alfa Slab One", serif; font-weight: 400;
    color: var(--white); font-size: 60px; line-height: 1; letter-spacing: 1px;
    transform: scaleX(0.6); white-space: nowrap;
  }
  .facility-photo {
    position: absolute; left: 0; top: 133px; width: 100%; height: 224px;
    background: linear-gradient(90deg, var(--steel-mid) 0%, var(--steel-light) 35%, #dfe3e8 60%, #b9bec6 80%, var(--steel-light) 100%);
  }
  .contact-band {
    position: absolute; left: 0; top: 368px; width: 100%; height: 65px;
    background: var(--navy);
    display: flex; align-items: center; padding: 0 32px;
    font-family: "Poppins", sans-serif; font-size: 42px; line-height: 1;
    white-space: nowrap;
  }
  .contact-label { color: var(--white); font-weight: 400; margin-right: 14px; }
  .contact-name { color: var(--green); font-weight: 700; }
  .contact-phone { margin-left: auto; display: flex; align-items: center; gap: 6px; color: var(--green); font-weight: 700; }
  .contact-phone svg { width: 36px; height: 36px; }
  .brand-band {
    position: absolute; left: 0; top: 433px; width: 100%; height: 146px;
    background: var(--green);
  }
  .brand-name {
    position: absolute; left: 31px; top: -4px;
    font-family: "Alfa Slab One", serif; font-size: 60px; color: var(--white);
    white-space: nowrap; line-height: 1.2;
  }
  .services {
    position: absolute; left: 32px; top: 62px;
    font-family: "Alfa Slab One", serif; font-size: 25px; line-height: 28px;
    color: var(--navy); white-space: nowrap;
  }
  .details {
    position: absolute; left: 425px; top: 64px;
    font-family: "Poppins", sans-serif; font-weight: 600; font-size: 23px;
    color: var(--navy); line-height: 27px;
  }
  .details li { list-style: none; display: flex; align-items: center; gap: 12px; white-space: nowrap; }
  .details svg { width: 20px; height: 20px; flex: none; }
</style>
</head>
<body>
  <div class="ad">
    <div class="headline-band">
      <h1 class="headline">STORE IT SAFELY. ACCESS IT EASILY.</h1>
    </div>
    <div class="facility-photo" role="img" aria-label="Photo of a clean indoor hallway lined with white roll-up storage unit doors"></div>
    <div class="contact-band">
      <span class="contact-label">Contact</span>
      <span class="contact-name">Daniel Marsh</span>
      <span class="contact-phone">
        <svg viewBox="0 0 36 36" aria-hidden="true">
          <circle cx="18" cy="18" r="18" fill="#fff"/>
          <path d="M12 9c1-.6 2-.4 2.6.5l2 3c.5.8.3 1.8-.4 2.4l-1.3 1c.9 2 2.5 3.7 4.5 4.6l1-1.3c.6-.7 1.6-.9 2.4-.4l3 2c.9.6 1.1 1.7.5 2.6l-1 1.5c-.8 1.1-2.200 1.6-3.5 1.1C15 24.6 11.4 21 10 14.2c-.3-1.3.1-2.6 1.1-3.4z" fill="#231d5c"/>
        </svg>
        3605550184
      </span>
    </div>
    <div class="brand-band">
      <div class="brand-name">Cedar Hollow Mini Storage</div>
      <p class="services">Indoor Storage Units +<br>Outdoor RV &amp; Boat Storage</p>
      <ul class="details">
        <li>
          <svg viewBox="0 0 20 20" aria-hidden="true"><circle cx="10" cy="10" r="10" fill="#fff"/><rect x="5" y="6.5" width="10" height="7" rx="1" fill="none" stroke="#6cbf1f" stroke-width="1.4"/><path d="M5.5 7l4.5 3.5L14.5 7" fill="none" stroke="#6cbf1f" stroke-width="1.4"/></svg>
          chministorage@mailbox.net
        </li>
        <li>
          <svg viewBox="0 0 20 20" aria-hidden="true"><circle cx="10" cy="10" r="10" fill="#fff"/><path d="M10 4.5a3.8 3.8 0 0 0-3.8 3.8c0 2.8 3.8 7 3.8 7s3.8-4.2 3.8-7A3.8 3.8 0 0 0 10 4.5z" fill="#6cbf1f"/><circle cx="10" cy="8.3" r="1.4" fill="#fff"/></svg>
          PO Box 40718, Harbor Point, OR 97412
        </li>
      </ul>
    </div>
  </div>
</body>
</html>
```